Startup of Management Company looking for Designers!

I am looking for an upscale website. Valmoreth will focus on Real Estate, Wealth Management, and Consulting,

Target Market(s)

investors, sellers of real estate, people looking to have their real estate management.
companies looking for consulting services

Number of Pages Required

5+ page

Font styles to use
Sans Serif

Requirements
Must have
• pictures, real.

```html
<!DOCTYPE html>
<html lang="en">
<head>
<meta charset="utf-8">
<title>Valmoreth — Real Estate, Wealth Management &amp; Consulting</title>
<link rel="stylesheet" href="https://fonts.googleapis.com/css2?family=Oswald:wght@400;500;600&family=Lato:wght@400;700&family=Rubik:wght@400;500&display=swap">
<style>
:root{
  --teal-dark:#0f4d50;
  --teal:#17595b;
  --teal-band:#1a4b4d;
  --teal-band-2:#1f5f61;
  --teal-panel:rgba(52,128,124,.9);
  --olive:#9fb21f;
  --ink:#111;
  --body:#333;
  --muted:#777;
  --mist:#e3ecea;
  --white:#fff;
}
*{box-sizing:border-box;margin:0;padding:0}
html,body{width:1200px;height:3895px;overflow:hidden}
body{position:relative;background:var(--white);font-family:'Lato',sans-serif;color:var(--body)}
.abs{position:absolute}
.photo{position:absolute;box-shadow:0 2px 6px rgba(0,0,0,.35)}
.lines{white-space:nowrap}

/* header */
.site-header{left:0;top:0;width:1200px;height:89px;background:var(--white)}
.brand{left:121px;top:24px;font-family:'Oswald',sans-serif;font-weight:600;font-size:27px;line-height:36px;color:var(--ink);letter-spacing:.3px}
.nav{left:399px;top:35px;display:flex;gap:40px;font-family:'Rubik',sans-serif;font-size:15px;line-height:20px;font-weight:500;color:#222}

/* hero */
.hero-photo{left:0;top:89px;width:1200px;height:600px;background:linear-gradient(180deg,#4d5d78 0%,#3b4a5e 35%,#3d5a34 75%,#2f4a22 100%)}
.phone-badge{left:890px;top:89px;width:198px;height:61px;background:var(--teal);display:flex;align-items:center;gap:14px;padding-left:18px;color:var(--white);font-family:'Rubik',sans-serif;font-size:18px}
.phone-badge .dot{width:34px;height:34px;border-radius:50%;background:var(--white);display:flex;align-items:center;justify-content:center}
.hero-panel{left:104px;top:280px;width:496px;height:533px;background:var(--teal-panel);padding:18px 41px}
.hero-title{font-family:'Oswald',sans-serif;font-weight:400;font-size:64px;line-height:66px;color:var(--white)}
.hero-rule{width:139px;height:3px;background:var(--olive);margin-top:21px}
.hero-text{margin-top:26px;font-size:17px;line-height:30px;color:var(--white)}
.btn-outline{display:inline-flex;align-items:center;justify-content:center;border:2px solid var(--white);color:var(--white);font-family:'Rubik',sans-serif;font-weight:500;font-size:17px;letter-spacing:.3px}
.hero-btn{left:144px;top:721px;width:170px;height:51px}

/* section heads */
.section-title{left:0;width:1200px;text-align:center;font-family:'Oswald',sans-serif;font-weight:600;font-size:37px;line-height:44px;color:var(--ink)}
.section-rule{height:3px;width:104px;left:548px;background:var(--teal)}

/* focus */
.focus-card{width:312px}
.focus-card .photo{position:relative;width:312px;height:201px}
.focus-card h3{font-family:'Oswald',sans-serif;font-weight:400;font-size:29px;line-height:40px;color:var(--ink);margin:8px 0 0 12px}
.focus-card p{font-size:17px;line-height:30px;margin:2px 0 0 12px;color:#333;white-space:nowrap}
.focus-card a{display:block;margin:10px 0 0 12px;font-family:'Rubik',sans-serif;font-size:12.5px;color:var(--teal);text-decoration:none;letter-spacing:.3px}

/* target bands */
.band-1{left:0;top:1662px;width:1200px;height:451px;background:var(--teal-band)}
.band-2{left:0;top:2113px;width:1200px;height:453px;background:var(--teal-band-2)}
.target-title{font-family:'Oswald',sans-serif;font-weight:400;font-size:38px;line-height:50px;color:var(--white)}
.target-text{font-size:17.5px;line-height:30px;color:var(--white);white-space:nowrap}

/* testimonials */
.quote-box{width:311px;height:176px;background:var(--white);border:2px solid #ddd;box-shadow:0 1px 4px rgba(0,0,0,.25);padding:14px 20px}
.quote-mark{font-family:'Oswald',sans-serif;font-size:30px;line-height:24px;color:var(--teal);font-style:italic}
.quote-box p{font-size:15px;line-height:30px;color:var(--muted);margin-top:8px;white-space:nowrap}
.quote-tail{position:absolute;left:26px;bottom:-20px}
.quote-name{font-family:'Oswald',sans-serif;font-size:18px;line-height:24px;color:var(--teal)}

/* contact */
.contact-band{left:0;top:3064px;width:1200px;height:744px;background:var(--mist)}
.map{left:110px;top:3154px;width:452px;height:438px;background:linear-gradient(135deg,#5f78c4 0%,#6c87c9 40%,#7ea66e 60%,#6f9a5c 100%)}
.map-pop{left:178px;top:3318px;width:242px;height:106px;background:var(--teal);color:var(--white);font-size:14.5px;line-height:30px;text-align:center;padding-top:8px;border-radius:3px}
.map-pop svg{position:absolute;left:112px;bottom:-13px}
.touch-title{left:653px;top:3142px;font-family:'Oswald',sans-serif;font-weight:600;font-size:37px;line-height:44px;color:var(--ink)}
.touch-rule{left:653px;top:3198px;width:104px;height:3px;background:var(--teal)}
.field{left:653px;width:393px;background:var(--white);border:1px solid #c9d4d2;border-radius:3px;font-family:'Rubik',sans-serif;font-size:13px;color:#333;padding:17px 14px}
.submit{left:653px;top:3553px;width:140px;height:49px;background:var(--teal);color:var(--white);font-family:'Rubik',sans-serif;font-weight:500;font-size:17px;display:flex;align-items:center;justify-content:center;letter-spacing:.5px}
.agent{left:117px;top:3640px;font-family:'Rubik',sans-serif;font-weight:500;font-size:17px;line-height:30px;color:var(--teal)}
.contact-line{left:117px;font-family:'Rubik',sans-serif;font-size:14px;font-weight:500;color:#222;display:flex;align-items:center;gap:10px}

/* footer */
.site-footer{left:0;top:3808px;width:1200px;height:87px;background:var(--teal-dark)}
.copyright{left:162px;top:3843px;font-size:13.5px;color:var(--white)}
.social{left:651px;top:3844px;display:flex;gap:10px}
.social span{width:12px;height:12px;border-radius:50%;background:var(--white)}
.chat{left:814px;top:3829px;width:268px;height:66px;background:#0b3a3c;color:var(--white);font-family:'Rubik',sans-serif;padding:14px 34px}
.chat strong{display:block;font-weight:400;font-size:12.5px}
.chat small{font-size:10.5px}
</style>
</head>
<body>

<header class="abs site-header">
  <div class="abs brand">VALMORETH</div>
  <nav class="abs nav"><span>HOME</span><span>REAL ESTATE</span><span>WEALTH MANAGEMENT</span><span>CONSULTING</span><span>CONTACT</span></nav>
</header>

<div class="abs hero-photo" role="img" aria-label="Photograph of a blue craftsman-style house with lit windows among tall pine trees at dusk"></div>
<div class="abs phone-badge">
  <span class="dot"><svg width="18" height="18" viewBox="0 0 24 24"><path fill="#17595b" d="M6.6 10.8a15.1 15.1 0 0 0 6.6 6.6l2.2-2.2c.3-.3.7-.4 1-.2 1.1.4 2.3.6 3.6.6.6 0 1 .4 1 1V20c0 .6-.4 1-1 1A17 17 0 0 1 3 4c0-.6.4-1 1-1h3.5c.6 0 1 .4 1 1 0 1.3.2 2.5.6 3.6.1.3 0 .7-.2 1z"/></svg></span>
  +120 555 0147
</div>
<section class="abs hero-panel">
  <h1 class="hero-title">Welcome &nbsp;to<br>Valmoreth</h1>
  <div class="hero-rule"></div>
  <p class="hero-text lines">Sed ut perspiciatis unde omnis iste natus error sit<br>voluptatem accusantium doloremque laudantium,<br>totam rem aperiam, eaque ipsa quae ab illo inventore<br>veritatis et quasi architecto beatae vitae dicta sunt<br>explicabo. Nemo enim ipsam voluptatem quia<br>voluptas sit aspernatur aut odit aut fugit, sed quia<br>consequuntur magni dolores eos qui ratione.</p>
</section>
<div class="abs btn-outline hero-btn">GET STARTED</div>

<h2 class="abs section-title" style="top:900px">OUR FOCUS AREA</h2>
<div class="abs section-rule" style="top:956px"></div>

<article class="abs focus-card" style="left:119px;top:991px">
  <div class="photo" role="img" aria-label="Photograph of a grey suburban house with a double garage" style="background:linear-gradient(180deg,#a9c2dc 0%,#5b6677 50%,#8a8f86 100%)"></div>
  <h3>Real Estate</h3>
  <p>Lorem ipsum dolor sit amet, cons<br>tetur adipiscing elit, sed do eiusmod<br>tempor incididunt ut labore et dolore<br>magna aliqua.</p>
  <a>LEARN MORE</a>
</article>
<article class="abs focus-card" style="left:444px;top:991px">
  <div class="photo" role="img" aria-label="Photograph of a calculator, compass, coins and a piggy bank on financial papers" style="background:linear-gradient(135deg,#3a3428 0%,#8a7a5c 50%,#c9b98f 100%)"></div>
  <h3>Wealth Management</h3>
  <p>Lorem ipsum dolor sit amet, cons<br>tetur adipiscing elit, sed do eiusmod<br>tempor incididunt ut labore et dolore<br>magna aliqua.</p>
  <a>LEARN MORE</a>
</article>
<article class="abs focus-card" style="left:769px;top:991px">
  <div class="photo" role="img" aria-label="Photograph of two consultants reviewing work at a desk computer" style="background:linear-gradient(135deg,#e8ecee 0%,#c7ced2 50%,#2d3440 100%)"></div>
  <h3>Consulting</h3>
  <p>Lorem ipsum dolor sit amet, cons<br>tetur adipiscing elit, sed do eiusmod<br>tempor incididunt ut labore et dolore<br>magna aliqua.</p>
  <a>LEARN MORE</a>
</article>

<h2 class="abs section-title" style="top:1474px">OUR TARGET ARE</h2>
<div class="abs section-rule" style="top:1538px"></div>

<div class="abs band-1"></div>
<div class="photo" role="img" aria-label="Photograph of business people shaking hands over an architectural building model" style="left:110px;top:1576px;width:467px;height:453px;background:linear-gradient(135deg,#f1f1f1 0%,#c9ccce 45%,#2b2e33 80%,#eaeaea 100%);border:2px solid #fff"></div>
<h3 class="abs target-title" style="left:623px;top:1720px">INVESTORS</h3>
<p class="abs target-text" style="left:623px;top:1779px">Lorem ipsum dolor sit amet, consectetur adipiscing elit,<br>sed do eiusmod tempor incididunt ut labore et dolore<br>magna aliqua. Ut enim ad minim veniam, quis nostrud<br>exercitation ullamco laboris nisi ut aliquip.</p>
<div class="abs btn-outline" style="left:623px;top:1931px;width:170px;height:51px">LEARN MORE</div>

<div class="abs band-2"></div>
<h3 class="abs target-title" style="left:106px;top:2190px">SELLERS OF REAL ESTATE</h3>
<p class="abs target-text" style="left:106px;top:2249px">Lorem ipsum dolor sit amet, consectetur adipiscing elit,<br>sed do eiusmod tempor incididunt ut labore et dolore<br>magna aliqua. Ut enim ad minim veniam, quis nostrud<br>exercitation ullamco laboris nisi ut aliquip.</p>
<div class="abs btn-outline" style="left:104px;top:2400px;width:171px;height:51px">LEARN MORE</div>
<div class="photo" role="img" aria-label="Photograph of a real estate agent showing a couple around a bright home interior" style="left:559px;top:2196px;width:466px;height:370px;background:linear-gradient(135deg,#c9b99a 0%,#8a8f98 40%,#6c7f9a 70%,#3f4b5a 100%);border:2px solid #fff"></div>

<h2 class="abs section-title" style="top:2654px">WHAT OUR CLIENTS THINK</h2>
<div class="abs section-rule" style="top:2706px"></div>

<div class="abs quote-box" style="left:118px;top:2743px">
  <div class="quote-mark">“</div>
  <p>Lorem ipsum dolor sit amet, conse<br>ctetur adipiscing elit, sed do eiusmod<br>tempor incididunt ut labore et dolore<br>magna aliqua.</p>
  <svg class="quote-tail" width="30" height="20" viewBox="0 0 30 20"><path d="M0 0 L15 19 L30 0" fill="#fff" stroke="#ccc" stroke-width="2"/></svg>
</div>
<div class="abs quote-name" style="left:142px;top:2941px">- Nora &amp; Elias Brandt</div>
<div class="abs quote-box" style="left:446px;top:2743px">
  <div class="quote-mark">“</div>
  <p>Lorem ipsum dolor sit amet, conse<br>ctetur adipiscing elit, sed do eiusmod<br>tempor incididunt ut labore et dolore<br>magna aliqua.</p>
  <svg class="quote-tail" width="30" height="20" viewBox="0 0 30 20"><path d="M0 0 L15 19 L30 0" fill="#fff" stroke="#ccc" stroke-width="2"/></svg>
</div>
<div class="abs quote-name" style="left:470px;top:2941px">- Nora &amp; Elias Brandt</div>
<div class="abs quote-box" style="left:772px;top:2743px">
  <div class="quote-mark">“</div>
  <p>Lorem ipsum dolor sit amet, conse<br>ctetur adipiscing elit, sed do eiusmod<br>tempor incididunt ut labore et dolore<br>magna aliqua.</p>
  <svg class="quote-tail" width="30" height="20" viewBox="0 0 30 20"><path d="M0 0 L15 19 L30 0" fill="#fff" stroke="#ccc" stroke-width="2"/></svg>
</div>
<div class="abs quote-name" style="left:796px;top:2941px">- Nora &amp; Elias Brandt</div>

<section class="abs contact-band"></section>
<div class="abs map" role="img" aria-label="Map showing the Atlantic region with Europe and Africa"></div>
<div class="abs map-pop">voluptatem accusantium<br>doloremque laudantium,<br>totam rem aperiam, eaque.
  <svg width="18" height="14" viewBox="0 0 18 14"><path d="M0 0 H18 L9 14z" fill="#17595b"/></svg>
</div>

<h2 class="abs touch-title">GET IN TOUCH</h2>
<div class="abs touch-rule"></div>
<div class="abs field" style="top:3214px;height:54px">First Name</div>
<div class="abs field" style="top:3279px;height:54px">Email</div>
<div class="abs field" style="top:3344px;height:54px">Phone</div>
<div class="abs field" style="top:3410px;height:114px">Message</div>
<div class="abs submit">SUBMIT</div>

<div class="abs agent">TO SPEAK WITH AN AGENT,<br>PLEASE CALL OR EMAIL US:</div>
<div class="abs contact-line" style="top:3704px">
  <svg width="15" height="12" viewBox="0 0 15 12"><rect width="15" height="12" rx="1" fill="#17595b"/><path d="M0 1 L7.5 7 L15 1" fill="none" stroke="#e3ecea" stroke-width="1.4"/></svg>info@valmoreth.com</div>
<div class="abs contact-line" style="top:3734px">
  <svg width="14" height="14" viewBox="0 0 24 24"><path fill="#17595b" d="M6.6 10.8a15.1 15.1 0 0 0 6.6 6.6l2.2-2.2c.3-.3.7-.4 1-.2 1.1.4 2.3.6 3.6.6.6 0 1 .4 1 1V20c0 .6-.4 1-1 1A17 17 0 0 1 3 4c0-.6.4-1 1-1h3.5c.6 0 1 .4 1 1 0 1.3.2 2.5.6 3.6.1.3 0 .7-.2 1z"/></svg>Tel: 120 555 0147</div>
<div class="abs contact-line" style="top:3764px">
  <svg width="15" height="14" viewBox="0 0 15 14"><rect x="3" y="0" width="9" height="5" fill="#17595b"/><rect x="0" y="5" width="15" height="9" rx="1" fill="#17595b"/><rect x="4" y="8" width="7" height="3" fill="#e3ecea"/></svg>Fax: 1800 555 0199</div>

<footer class="abs site-footer"></footer>
<div class="abs copyright">© Copyrights 2021 <b>Valmoreth</b> &nbsp;| &nbsp; All Rights Reserved</div>
<div class="abs social"><span></span><span></span><span></span></div>
<div class="abs chat"><strong>CHAT WITH US</strong><small>We'll reply as soon as we can</small>
  <svg class="abs" style="right:22px;top:28px" width="12" height="8" viewBox="0 0 12 8"><path d="M1 7 L6 2 L11 7" fill="none" stroke="#fff" stroke-width="1.5"/></svg>
</div>

</body>
</html>
```